New Business card design to reflect rebrand

I would like a business card design with a good base colour for our new logo and also a placeholder for a profile pic of the card holder. the design needs to be editable to the point that we can easily change the picture of the person and use that design for printmoor etc. we are looking at a metalic finish business card so will need a good base colour to bring out the finish.

Target Market(s)

prospective customers

Industry/Entity Type

Business

Contact Information for Business Card

I would like one editable design that we can change the name of the card holder and profile picture. The design need to be in a format that be send to printmoor etc.

Our address is Fenwick Lodge, Mill Lane, Ashcombe Green, RG41 3TQ Tel no. 01632 960417

Requirements
Must have
• place holder for a profile pic for the card holder. in AI or preferably PSD format

```html
<!DOCTYPE html>
<html lang="en">
<head>
<meta charset="utf-8">
<title>Corvane Workplace Services – Business Card</title>
<link rel="stylesheet" href="https://fonts.googleapis.com/css2?family=Michroma&family=Montserrat:wght@400;600&display=swap">
<style>
  :root {
    --orange: #ee6423;
    --navy: #3a4a63;
    --white: #ffffff;
    --stage: #e4e4e4;
    --photo-top: #8a8f99;
    --photo-bottom: #3b3f4a;
  }
  * { box-sizing: border-box; margin: 0; padding: 0; }
  html, body { width: 1200px; height: 900px; overflow: hidden; }
  body {
    background: var(--stage);
    font-family: "Montserrat", sans-serif;
    position: relative;
  }
  .card {
    position: absolute;
    left: 250px;
    width: 700px;
    height: 400px;
    box-shadow: 0 6px 18px rgba(0,0,0,0.25);
  }
  .card--front { top: 40px; background: var(--orange); }
  .card--back  { top: 460px; background: var(--white); }

  /* front */
  .front-brand {
    position: absolute;
    inset: 0;
    display: flex;
    flex-direction: column;
    align-items: center;
    justify-content: center;
    color: var(--white);
    font-family: "Michroma", sans-serif;
  }
  .front-brand .brand-name { font-size: 46px; letter-spacing: 2px; line-height: 1.1; }
  .front-brand .brand-sub { font-size: 17px; letter-spacing: 5px; margin-top: 8px; }
  .front-brand .brand-web {
    font-family: "Montserrat", sans-serif;
    font-size: 16px; margin-top: 16px; letter-spacing: 0.5px;
  }

  /* back */
  .back-brand {
    position: absolute;
    right: 40px; top: 40px;
    text-align: right;
    font-family: "Michroma", sans-serif;
  }
  .back-brand .brand-name { color: var(--navy); font-size: 32px; letter-spacing: 1px; line-height: 1.1; }
  .back-brand .brand-sub { color: var(--orange); font-size: 12px; letter-spacing: 3.5px; margin-top: 6px; }

  .address {
    position: absolute;
    right: 40px; top: 142px;
    text-align: right;
    color: var(--navy);
    font-style: normal;
    font-size: 14px; line-height: 1.45;
  }
  .rule--address {
    position: absolute;
    left: 330px; right: 40px; top: 192px;
    height: 2px;
    background: var(--orange);
  }

  .contacts {
    position: absolute;
    right: 36px; top: 208px;
    list-style: none;
    color: var(--navy);
    font-size: 14px; line-height: 1.6;
  }
  .contacts li { display: flex; justify-content: flex-end; align-items: center; gap: 8px; }
  .contacts svg { width: 11px; height: 11px; }
  .contacts .accent { color: var(--orange); font-weight: 600; }

  .portrait-frame {
    position: absolute;
    left: 40px; top: 120px;
    width: 210px; height: 200px;
    border: 2px solid var(--navy);
    padding: 10px;
  }
  .portrait {
    width: 100%; height: 100%;
    background: linear-gradient(180deg, var(--photo-top), var(--photo-bottom));
  }

  .holder {
    position: absolute;
    left: 40px; top: 332px;
    font-family: "Michroma", sans-serif;
  }
  .holder-line {
    display: flex;
    align-items: center;
    gap: 12px;
  }
  .holder-name {
    color: var(--orange);
    font-size: 20px;
    letter-spacing: 1px;
    white-space: nowrap;
  }
  .holder-rule {
    width: 150px;
    height: 2px;
    background: var(--orange);
  }
  .holder-role { color: var(--navy); font-size: 14px; letter-spacing: 1px; margin-top: 4px; }
</style>
</head>
<body>

<section class="card card--front">
  <div class="front-brand">
    <div class="brand-name">CORVANE</div>
    <div class="brand-sub">WORKPLACE SERVICES</div>
    <div class="brand-web">www.corvane.com</div>
  </div>
</section>

<section class="card card--back">
  <div class="back-brand">
    <div class="brand-name">CORVANE</div>
    <div class="brand-sub">WORKPLACE SERVICES</div>
  </div>

  <address class="address">
    Fenwick Lodge, Mill Lane<br>
    Ashcombe Green, RG41 3TQ
  </address>
  <div class="rule--address"></div>

  <ul class="contacts">
    <li>01632 960417
      <svg viewBox="0 0 12 12"><path d="M2.5 1 L4.5 1 L5.2 3.4 L4 4.4 Q5 6.8 7.6 8 L8.6 6.8 L11 7.5 L11 9.5 Q10.5 11 9 11 Q1 10 1 3 Q1 1.5 2.5 1Z" fill="var(--orange)"/></svg>
    </li>
    <li>info@corvane.com
      <svg viewBox="0 0 12 12"><rect x="1" y="2.5" width="10" height="7" fill="none" stroke="var(--orange)" stroke-width="1.2"/><path d="M1 2.5 L6 6.5 L11 2.5" fill="none" stroke="var(--orange)" stroke-width="1.2"/></svg>
    </li>
    <li><span>www.<span class="accent">corvane</span>.com</span>
      <svg viewBox="0 0 12 12"><circle cx="6" cy="6" r="5" fill="var(--orange)"/><path d="M1 6 H11 M6 1 Q3 6 6 11 M6 1 Q9 6 6 11" fill="none" stroke="var(--white)" stroke-width="0.8"/></svg>
    </li>
  </ul>

  <div class="portrait-frame">
    <div class="portrait" role="img" aria-label="Profile photo of the card holder"></div>
  </div>

  <div class="holder">
    <div class="holder-line">
      <div class="holder-name">MAREK HOLLOWAY</div>
      <div class="holder-rule"></div>
    </div>
    <div class="holder-role">DIRECTOR</div>
  </div>
</section>

</body>
</html>
```